Business Card Design for my Real Estate Investing Company

This is for a Real Estate Investing Company that will be serving the Las Vegas Valley. Id like the following slogan included: "Investing in Our Community" I have attached my logo. You will see the color tones I'm interested in..in my logo. I would like the card to be double-sided with a modern, professional look.
Target Market(s)
Homeowners, banks, real estate industry
Industry/Entity Type
Real Estate
Contact Information for Business Card
name: Dale Pruitt
position: Managing Member
address: 4812 Corvane Pkwy ste 207-300
N. Las Vegas, NV 89517
phone: (702) 555-0143
fax: (702) 555-0187
email: OakridgeHousePurchaser@examplemail.com
web: OakridgeHousePurchasers.example
*At the bottom of the card I would like....
We buy houses for cash....no repairs, no commissions, no fees!
Logo Text
OAKRIDGE HOUSE PURCHASERS "Investing in Our Community"
Font styles to use
Other font styles liked:
- Lora
Requirements
Must have
- On the back of the card, i'd like to have my logo large and the following statements:
- Are you considering selling your home? Want a simple, hassle-free transaction? We can help! We buy houses for cash and can close quickly! No need to do any repairs, no realtor commissions, no closing costs.....and no headaches. Let us help you with your real estate needs...!
Nice to have
- multiple colors 2 two tone on front and back

```html
<!DOCTYPE html>
<html lang="en">
<head>
<meta charset="utf-8">
<title>Oakridge House Purchasers – Business Card</title>
<link rel="stylesheet" href="https://fonts.googleapis.com/css2?family=Lora:ital,wght@0,400;0,700;1,400&display=swap">
<style>
  :root {
    --stage: #e7e4df;
    --card-blue: #0c55a3;
    --card-dark: #333333;
    --ink-white: #ffffff;
    --rule: rgba(255,255,255,0.45);
    --tagline-blue: #0c55a3;
    --band-white: #ffffff;
  }
  * { margin: 0; padding: 0; box-sizing: border-box; }
  html, body {
    width: 1200px; height: 1000px; overflow: hidden;
    background: var(--stage);
    font-family: "Lora", Georgia, serif;
  }
  .canvas { position: relative; width: 1200px; height: 1000px; }

  .card {
    position: absolute; left: 243px; width: 708px; height: 404px;
    box-shadow: 0 4px 14px rgba(0,0,0,0.25);
    color: var(--ink-white);
  }
  .card-front { top: 65px; background: var(--card-blue); }
  .card-back { top: 533px; background: var(--card-dark); }

  .front-brand {
    position: absolute; right: 33px; top: 52px; text-align: right;
  }
  .front-brand .brand-name {
    font-size: 25px; font-weight: 400; letter-spacing: 0.5px; line-height: 1.1;
  }
  .front-brand .brand-slogan {
    margin-top: 8px; font-style: italic; font-size: 13px; letter-spacing: 2.6px;
  }

  .person { position: absolute; left: 33px; top: 160px; }
  .person-name { font-size: 21px; font-weight: 700; line-height: 1.2; }
  .person-title { font-size: 16px; margin-top: 2px; }

  .divider {
    position: absolute; left: 33px; right: 33px; top: 218px;
    border-top: 1px solid var(--rule);
  }

  .contact-list {
    position: absolute; left: 33px; top: 230px; list-style: none;
    font-size: 16px; line-height: 22.7px;
  }
  .contact-list li { display: flex; align-items: center; gap: 6px; }
  .contact-list svg { width: 13px; height: 13px; fill: var(--ink-white); flex: none; }

  .address {
    position: absolute; right: 33px; top: 275px; text-align: right;
    font-size: 16px; line-height: 22.7px;
  }

  .tagline-band {
    position: absolute; left: 0; right: 0; bottom: 0; height: 54px;
    background: var(--band-white);
    display: flex; align-items: center; justify-content: flex-end; padding-right: 31px;
  }
  .tagline {
    color: var(--tagline-blue); font-style: italic; font-size: 18.5px; letter-spacing: 1.1px;
  }

  .back-brand {
    position: absolute; left: 0; right: 0; top: 165px; text-align: center;
  }
  .back-brand .brand-name {
    font-size: 37px; font-weight: 400; letter-spacing: 1px; line-height: 1.1;
  }
  .back-brand .brand-slogan {
    margin-top: 14px; font-style: italic; font-size: 17px; letter-spacing: 4.3px;
  }
</style>
</head>
<body>
<main class="canvas">

  <section class="card card-front" aria-label="Card front">
    <div class="front-brand">
      <div class="brand-name">OAKRIDGE HOUSE PURCHASERS</div>
      <div class="brand-slogan">"Investing in Our Community"</div>
    </div>

    <div class="person">
      <div class="person-name">Dale Pruitt</div>
      <div class="person-title">Managing Member</div>
    </div>

    <div class="divider"></div>

    <ul class="contact-list">
      <li>
        <svg viewBox="0 0 16 16" aria-hidden="true"><path d="M3.6 1.5l2.3 2.6-1.2 1.8c.9 1.9 2.4 3.4 4.3 4.3l1.8-1.2 2.6 2.3-1.3 2.4C7 13.6 2.4 9 1.2 3l2.4-1.5z"/></svg>
        (702) 555-0143
      </li>
      <li>
        <svg viewBox="0 0 16 16" aria-hidden="true"><path d="M4 1h8v4H4zM1 6h14v6h-3v3H4v-3H1zM5 10v4h6v-4z"/></svg>
        (702) 555-0187
      </li>
      <li>
        <svg viewBox="0 0 16 16" aria-hidden="true"><path d="M1 3h14v1L8 9 1 4zM1 5.5l7 5 7-5V13H1z"/></svg>
        OakridgeHousePurchaser@examplemail.com
      </li>
      <li>
        <svg viewBox="0 0 16 16" aria-hidden="true"><path d="M8 1a7 7 0 100 14A7 7 0 008 1zm0 1.3c.9 0 1.9 1.6 2.2 4.1H5.8C6.1 3.9 7.1 2.3 8 2.3zM2.4 7.4h2.3c0 .4 0 .8 0 1.2H2.4zm0 0M5.8 9.6h4.4C9.9 12.1 8.9 13.7 8 13.7S6.1 12.1 5.8 9.6zM2.5 6.4a5.7 5.7 0 013-3.6 9 9 0 00-.8 3.6zm8.8 0a9 9 0 00-.8-3.6 5.7 5.7 0 013 3.6zm0 1h2.3v1.2h-2.3zM5.7 7.4h4.6v1.2H5.7zm-3.2 2.2h2.2a9 9 0 00.8 3.6 5.7 5.7 0 01-3-3.6zm8.8 0h2.2a5.7 5.7 0 01-3 3.6 9 9 0 00.8-3.6z"/></svg>
        OakridgeHousePurchasers.example
      </li>
    </ul>

    <address class="address" style="font-style:normal">
      4812 Corvane Pkwy ste 207-300<br>
      N. Las Vegas, NV 89517
    </address>

    <div class="tagline-band">
      <p class="tagline">We buy houses for cash....no repairs, no commissions, no fees!</p>
    </div>
  </section>

  <section class="card card-back" aria-label="Card back">
    <div class="back-brand">
      <div class="brand-name">OAKRIDGE HOUSE PURCHASERS</div>
      <div class="brand-slogan">"Investing in Our Community"</div>
    </div>
  </section>

</main>
</body>
</html>
```